Creative Desing -Fishing E-com subscription website

Looking for a modern, creative design for the fishing subscription box.
Something with funny, interesting vectors but not too noisy design.
Name of the store is ReelWildAlways or ReelWild4ever. I would like the website to be more focused around gift boxes - see example here https://brambleparcelco.example/
Landing part of the page should be 'sign up' type section. Show a picture of a gift box, or a fishing bowl, with gifts visible somewhere (inside or next to the box?). Have two buttons: GIVE and GET. TItle should be something like "Fishing Gear Every Month"
Section 2: Next section (once use scrolls down from the main page) whould be "discover" type section which would highlight the newest arrivals / gift boxes available for the fish that is in season for example (again with a link to offer to shop - see this website as example https://www.quillwearhub.example/). Can be two newwest additions (left and right side of page)
Section 3 (scroll down more)
can be again two sections with the latest News/Blog on the left and a latest Picture/Video on the right (see bottom of this page https://www.quillwearhub.example/)
In addition to all this, can we have "How it Works" running to the side - this would entice people to scroll down. Kind of like steps (1, 2, 3) with each leading the person to scroll one page. Step 1: Pick your box - S, M, L. Step 2 can be frequency - monthly, quarterly, step 3 can be subscription duration - month-month, 6 months, 1 year. This can be a fishing lure going down the bottom of the website and at the very bottom "catching" the fish and havin the "GET" button

```html
<!DOCTYPE html>
<html lang="en">
<head>
<meta charset="utf-8">
<title>ReelWild4ever — Fishing Gear Every Month</title>
<link rel="stylesheet" href="https://fonts.googleapis.com/css2?family=Oswald:wght@300;400;500&family=Lato:wght@400;700&display=swap">
<style>
:root{
  --ink:#2b2b2b;
  --white:#ffffff;
  --nav-bg:#ffffff;
  --wood-dark:#1d3b43;
  --wood-mid:#3f6870;
  --green:#3f9a2e;
  --magenta:#c2248c;
  --blue:#1c6f9b;
  --panel-dark:#3a3a3a;
  --yellow:#e4e34a;
  --pink:#ef8fcf;
  --sky:#8fdcf5;
  --navy:#0f1c45;
  --mail-bg:#e7e7e7;
  --footer:#2f2f2f;
  --gold:#f1d96a;
}
*{box-sizing:border-box;margin:0;padding:0}
html,body{width:1200px;height:2812px;overflow:hidden}
body{position:relative;font-family:"Lato",sans-serif;color:var(--ink);background:var(--white)}
.ph{position:absolute;display:block}

/* top navigation */
.topbar{position:absolute;left:0;top:0;width:1200px;height:100px;background:var(--nav-bg)}
.brand{position:absolute;left:24px;top:10px;font:700 22px "Lato",sans-serif;color:var(--ink)}
.account-links{position:absolute;right:24px;top:14px;display:flex;gap:28px;font:400 14px "Lato",sans-serif;text-transform:uppercase}
.main-nav{position:absolute;left:24px;top:52px;display:flex;gap:30px;font:400 16px "Lato",sans-serif;text-transform:uppercase}

/* hero */
.hero{position:absolute;left:0;top:100px;width:1200px;height:412px;
  background:radial-gradient(ellipse at 50% 45%,var(--wood-mid),var(--wood-dark) 75%)}
.hero-title{position:absolute;left:0;width:1200px;top:14px;text-align:center;font:500 54px "Oswald",sans-serif;color:var(--white);letter-spacing:1px}
.hero-sub{position:absolute;left:0;width:1200px;top:80px;text-align:center;font:italic 400 20px "Lato",sans-serif;color:var(--white)}
.btn{position:absolute;top:124px;width:126px;height:60px;color:var(--white);font:500 26px "Oswald",sans-serif;display:flex;align-items:center;justify-content:center}
.btn-give{left:444px;background:var(--green)}
.btn-get{left:622px;background:var(--magenta)}

/* new arrivals */
.arrivals-title{position:absolute;left:0;width:1200px;top:560px;text-align:center;font:400 56px "Oswald",sans-serif;color:var(--ink)}
.arrival{position:absolute;top:640px;width:320px;height:270px}
.arrival .shot{position:absolute;left:0;top:0;width:320px;height:200px;border-radius:8px}
.arrival .num{position:absolute;left:0;top:216px}
.arrival .caption{position:absolute;left:60px;top:226px;font-size:15px;white-space:nowrap}
.rule{position:absolute;top:256px;height:3px;width:280px;left:40px}

.num{width:48px;height:48px;border-radius:50%;color:var(--white);font:500 24px "Oswald",sans-serif;display:flex;align-items:center;justify-content:center;z-index:1}

/* split panels */
.news{position:absolute;left:0;top:928px;width:608px;height:1324px;background:var(--panel-dark);color:var(--white)}
.panel-head{position:absolute;font:400 52px "Oswald",sans-serif}
.news .fresh{left:56px;top:50px;color:var(--yellow)}
.news .reels{left:56px;top:744px;color:var(--pink)}
.story{position:absolute;left:60px;width:500px}
.story .thumb{position:absolute;left:0;top:0;width:196px;height:196px;border-radius:50%}
.story h3{position:absolute;left:232px;top:0;width:270px;font:700 21px "Lato",sans-serif;color:var(--yellow)}
.story p{position:absolute;left:232px;top:60px;width:270px;font-size:15px;line-height:1.35}
.story .more{position:absolute;left:232px;top:200px;font:700 18px "Lato",sans-serif}
.reel-shot{position:absolute;left:60px;top:852px;width:480px;height:280px}
.reel-caption{position:absolute;left:60px;top:1158px;width:500px;font:700 20px "Lato",sans-serif;line-height:1.35}
.reel-caption span{color:var(--pink)}

.how{position:absolute;left:608px;top:928px;width:592px;height:1324px;
  background:linear-gradient(180deg,var(--sky) 0%,#6fb9de 38%,#25407a 70%,var(--navy) 100%)}
.how .panel-head{left:152px;top:60px;color:var(--ink);font-size:60px}
.how-line{position:absolute;left:62px;top:172px;width:3px;height:880px;background:var(--white)}
.step{position:absolute;left:40px;width:520px}
.step .num{position:absolute;left:0;top:0}
.step h4{position:absolute;left:88px;top:6px;white-space:nowrap;font:400 28px "Lato",sans-serif;text-transform:uppercase}
.step ul{position:absolute;left:88px;top:56px;list-style:none;font-size:19px;line-height:42px;color:var(--white);white-space:nowrap}
.sizes{position:absolute;left:128px;top:232px;font-size:19px;line-height:30px;color:var(--ink);display:grid;grid-template-columns:90px auto}
.box-shot{position:absolute;left:132px;top:336px;width:300px;height:176px}
.cal-shot{position:absolute;left:124px;top:744px;width:220px;height:208px}

/* mailing list */
.mailing{position:absolute;left:0;top:2252px;width:1200px;height:408px;background:var(--mail-bg)}
.mailing h2{position:absolute;left:200px;top:40px;font:300 42px "Lato",sans-serif;color:#555}
.field{position:absolute;left:0;width:1200px;height:30px}
.field label{position:absolute;right:524px;top:4px;font-size:19px}
.field span{position:absolute;left:700px;top:0;width:400px;height:30px;background:var(--white);border:1px solid #999}

/* footer */
.footer{position:absolute;left:0;top:2660px;width:1200px;height:152px;background:var(--footer);color:var(--white)}
.footer-nav{position:absolute;left:48px;top:30px;display:flex;gap:50px;font-size:19px;text-transform:uppercase}
.footer-nav .right{margin-left:190px}
.copyright{position:absolute;left:0;width:1200px;top:110px;text-align:center;font-size:18px}
</style>
</head>
<body>

<header class="topbar">
  <div class="brand">ReelWild4ever</div>
  <nav class="account-links"><span>Sign in / Create account</span><span>Redeem a gift</span><span>Help</span></nav>
  <nav class="main-nav"><span>Plans</span><span>Gifts</span><span>Shop</span><span>Blog</span></nav>
</header>

<section class="hero">
  <h1 class="hero-title">FISHING GEAR EVERY MONTH</h1>
  <p class="hero-sub">Lorem ipsum dolor sit consectetur vel lorem denim</p>
  <span class="ph" role="img" aria-label="Pink fishing lure hanging on a line" style="left:200px;top:150px;width:90px;height:190px;border-radius:40px;background:linear-gradient(180deg,#e493c4,#8a4f7b)"></span>
  <span class="ph" role="img" aria-label="Green and yellow fish lure" style="left:860px;top:150px;width:120px;height:170px;border-radius:50px;background:linear-gradient(160deg,#f0c640,#2f8a3e)"></span>
  <a class="btn btn-give">GIVE</a>
  <a class="btn btn-get">GET</a>
  <span class="ph" role="img" aria-label="Open cardboard gift box filled with fishing tackle" style="left:450px;top:250px;width:320px;height:140px;background:linear-gradient(180deg,#d8b98d,#9d7b50);border-radius:4px"></span>
</section>

<h2 class="arrivals-title">NEW ARRIVALS</h2>

<div class="arrival" style="left:80px">
  <span class="shot ph" role="img" aria-label="Yellow spinnerbait lure" style="background:radial-gradient(circle,#e8e56a,#fafafa 70%)"></span>
  <div class="rule" style="background:var(--magenta)"></div>
  <span class="num" style="background:var(--magenta)">1</span>
  <span class="caption">Lorem, ipsum dolor, consectetur</span>
</div>
<div class="arrival" style="left:440px">
  <span class="shot ph" role="img" aria-label="Realistic perch swimbait lure" style="background:radial-gradient(circle,#7f9a4a,#fafafa 70%)"></span>
  <div class="rule" style="background:var(--green)"></div>
  <span class="num" style="background:var(--green)">2</span>
  <span class="caption">Lorem, ipsum dolor, consectetur</span>
</div>
<div class="arrival" style="left:800px">
  <span class="shot ph" role="img" aria-label="Brown and gold crankbait lure" style="background:radial-gradient(circle,#a07a3a,#fafafa 70%)"></span>
  <div class="rule" style="background:var(--blue)"></div>
  <span class="num" style="background:var(--blue)">3</span>
  <span class="caption">Lorem, ipsum dolor, consectetur</span>
</div>

<section class="news">
  <h2 class="panel-head fresh">FRESH CATCH</h2>
  <article class="story" style="top:156px">
    <span class="thumb ph" role="img" aria-label="Green frog topwater lure" style="background:radial-gradient(circle,#7bbf4c,#e9efe3 70%)"></span>
    <h3>Fusce placerat risus sit amet</h3>
    <p>Morbi pellentesque odio et nulla interdum viverra. Nam suscipit, eros sit vulputate ultricies, libero odio mollis justo, nec varius felis odio at mi. Sed felis nisl, congue at finibus in, porttitor at elit.</p>
    <span class="more">Read more :</span>
  </article>
  <article class="story" style="top:452px">
    <span class="thumb ph" role="img" aria-label="Assorted tackle in a clear storage box" style="background:radial-gradient(circle,#9fb6cf,#eef1f5 70%)"></span>
    <h3>Praesent vel molestie mi.</h3>
    <p>In cursus, felis non pretium molestie, tellus lacus facilisis metus, ut accumsan nisi nulla accumsan risus. Etiam id pharetra ante. Nunc sit amet ante vitae nibh facilisis pretium arcu eu hendrerit.</p>
    <span class="more">Read more :</span>
  </article>
  <h2 class="panel-head reels">LATEST REELS</h2>
  <span class="reel-shot ph" role="img" aria-label="Misty river in a sunlit forest" style="background:linear-gradient(180deg,#cfe3c7,#5f8a55 55%,#2e4a35)"></span>
  <p class="reel-caption"><span>In cursus, felis non pretium molestie,</span> tellus lacus facilisis metus, ut accumsan nisi nulla accumsan risus. Etiam id pharetra ante. Nunc sit amet ante</p>
</section>

<section class="how">
  <h2 class="panel-head">HOW IT WORKS</h2>
  <div class="how-line"></div>
  <div class="step" style="top:160px">
    <span class="num" style="background:var(--magenta)">1</span>
    <h4 style="color:var(--magenta)">Pick your box</h4>
  </div>
  <div class="sizes"><span>Small</span><span>( 12" x 6" x 3" )</span><span>Medium</span><span>( 18" x 9" x 6" )</span><span>Large</span><span>( 24" x 12" x 12" )</span></div>
  <span class="box-shot ph" role="img" aria-label="Closed cardboard shipping box" style="background:linear-gradient(180deg,#e6cfa8,#b8976a)"></span>
  <div class="step" style="top:552px">
    <span class="num" style="background:var(--gold);color:var(--ink)">2</span>
    <h4 style="color:var(--gold)">How often do you want it?</h4>
    <ul><li>Monthly</li><li>Quarterly</li><li>Yearly</li></ul>
  </div>
  <span class="cal-shot ph" role="img" aria-label="Wall calendar page" style="background:linear-gradient(180deg,#ffffff,#d9d9d9)"></span>
  <div class="step" style="top:1036px">
    <span class="num" style="background:var(--sky);color:var(--ink)">3</span>
    <h4 style="color:var(--white)">Choose&nbsp; subscription plan</h4>
    <ul><li>Monthly</li><li>Quarterly</li><li>Semi-Annual</li><li>Yearly</li></ul>
  </div>
</section>

<section class="mailing">
  <h2>JOIN OUR MAILING LIST</h2>
  <div class="field" style="top:118px"><label>Email</label><span></span></div>
  <div class="field" style="top:166px"><label>Full Name</label><span></span></div>
  <div class="field" style="top:214px"><label>Contact Number</label><span></span></div>
  <div class="field" style="top:262px"><label>Postal Address</label><span></span></div>
  <div class="field" style="top:310px"><span></span></div>
</section>

<footer class="footer">
  <nav class="footer-nav"><span>Plans</span><span>Gifts</span><span>Shop</span><span>Blog</span><span class="right">Sign-in / Create account</span><span>Redeem a gift</span><span>Help</span></nav>
  <p class="copyright">Copy right &nbsp; ReelWild4ever</p>
</footer>

</body>
</html>
```